Set of 6 Icons and buttons required

We have written a windows based app which gives clients access to reports etc.

We are a multichannel epos company

We require 6 buttons and icons along with a suggested font to use and a background for the form.

I have attatched a mock up of what we require from the chosen designer.

The buttons are as follows :

Stockcard ( This is a program which customers can enter stock and check stock levels etc )

Reports ( as the title says )

Stock ( This for making adjustments )

Goods ( this is for booking goods in )

Settings ( As title says )

Help ( As title says )

Dimensions
---------------

The form : 296x268
Buttons : 218x36
Icons on button : 32x32
Text size : Size 10

If you look at the attatched document this is something I put together just to show what we are looking once we put all the components together

Our website is q-lumora.co.uk

Target Market(s)

B2B

Industry/Entity Type

It Company

```html
<!DOCTYPE html>
<html lang="en">
<head>
<meta charset="utf-8">
<title>Q-Lumora launcher</title>
<link href="https://fonts.googleapis.com/css2?family=Noto+Sans:wght@700&display=swap" rel="stylesheet">
<style>
  :root {
    --bg-top: #0f285f;
    --bg-bottom: #4b74c3;
    --panel: #4e4e4e;
    --panel-edge: #5a5a5a;
    --btn-light: #f4f4f4;
    --btn-dark: #c9c9c9;
    --btn-text: #454545;
    --active-light: #0a74c0;
    --active-dark: #00508e;
    --icon-disc: #4a4a4a;
    --brand-text: #d8d8d8;
    --brand-square: #1f5fa8;
  }
  * { box-sizing: border-box; margin: 0; padding: 0; }
  html, body { width: 1200px; height: 1117px; overflow: hidden; }
  body {
    background: linear-gradient(to bottom, var(--bg-top), var(--bg-bottom));
    font-family: "Noto Sans", sans-serif;
    position: relative;
  }
  .launcher {
    position: absolute;
    left: 339px; top: 323px;
    width: 522px; height: 470px;
    background: var(--panel);
    border: 1px solid var(--panel-edge);
  }
  .close-btn {
    position: absolute; left: 489px; top: 13px;
    width: 20px; height: 20px;
  }
  .brand-name {
    position: absolute;
    left: 57px; top: 215px;
    transform: translate(-50%, -50%) rotate(-90deg);
    color: var(--brand-text);
    font-weight: 700;
    font-size: 26px;
    letter-spacing: 5px;
    white-space: nowrap;
    line-height: 1;
  }
  .brand-square {
    position: absolute; left: 18px; top: 375px;
    width: 78px; height: 78px;
    background: var(--brand-square);
  }
  .menu { list-style: none; position: absolute; left: 120px; top: 47px; }
  .menu-item {
    width: 395px; height: 65px;
    margin-bottom: 4px;
    display: flex; align-items: center;
    background: linear-gradient(to bottom, var(--btn-light), var(--btn-dark));
    color: var(--btn-text);
    font-weight: 700; font-size: 24px;
  }
  .menu-item.is-active {
    background: linear-gradient(to bottom, var(--active-light), var(--active-dark));
    color: #fff;
  }
  .menu-icon { width: 58px; height: 58px; margin: 0 9px 0 5px; flex: none; }
</style>
</head>
<body>
  <div class="launcher">
    <svg class="close-btn" viewBox="0 0 20 20" aria-label="Close">
      <path d="M4 4 L16 16 M16 4 L4 16" stroke="#e6e6e6" stroke-width="4" stroke-linecap="round"/>
    </svg>
    <div class="brand-name">Q-LUMORA</div>
    <div class="brand-square"></div>

    <ul class="menu">
      <li class="menu-item">
        <svg class="menu-icon" viewBox="0 0 32 32"><circle cx="16" cy="16" r="16" fill="var(--icon-disc)"/>
          <rect x="8" y="9" width="16" height="14" fill="none" stroke="#fff" stroke-width="1.5"/>
          <path d="M10 12.5h12M10 15h12M10 17.5h12M10 20h12" stroke="#fff" stroke-width="1.2"/></svg>
        Stockcard
      </li>
      <li class="menu-item">
        <svg class="menu-icon" viewBox="0 0 32 32"><circle cx="16" cy="16" r="16" fill="var(--icon-disc)"/>
          <path d="M16 6 A10 10 0 1 0 26 16 L16 16 Z" fill="#fff"/>
          <path d="M14 9 L14 22 M14 16 L20 10 M15 16 L21 22" stroke="var(--icon-disc)" stroke-width="2"/></svg>
        Reports
      </li>
      <li class="menu-item is-active">
        <svg class="menu-icon" viewBox="0 0 32 32"><circle cx="16" cy="16" r="16" fill="#fff"/>
          <path d="M6 19 L10 14 L13 18 L17 13 L20 17 L23 13 L26 16" fill="none" stroke="#0a6cb4" stroke-width="2" stroke-linejoin="round"/></svg>
        Stock
      </li>
      <li class="menu-item">
        <svg class="menu-icon" viewBox="0 0 32 32"><circle cx="16" cy="16" r="16" fill="var(--icon-disc)"/>
          <rect x="9" y="15" width="6" height="8" fill="#fff"/><rect x="16" y="9" width="7" height="6" fill="#fff"/>
          <rect x="16" y="16" width="7" height="7" fill="#fff"/></svg>
        Goods
      </li>
      <li class="menu-item">
        <svg class="menu-icon" viewBox="0 0 32 32"><circle cx="16" cy="16" r="16" fill="var(--icon-disc)"/>
          <g stroke="#fff" stroke-width="3.5" stroke-linecap="round">
            <path d="M16 6v20M6 16h20M9 9l14 14M23 9L9 23"/></g>
          <circle cx="16" cy="16" r="7" fill="#fff"/><circle cx="16" cy="16" r="3" fill="var(--icon-disc)"/></svg>
        Settings
      </li>
      <li class="menu-item">
        <svg class="menu-icon" viewBox="0 0 32 32"><circle cx="16" cy="16" r="16" fill="var(--icon-disc)"/>
          <path d="M11.5 12.5 A4.5 4.5 0 1 1 17.5 16.5 C16 17.3 16 18 16 20" fill="none" stroke="#fff" stroke-width="3" stroke-linecap="round"/>
          <circle cx="16" cy="24" r="2" fill="#fff"/></svg>
        Help
      </li>
    </ul>
  </div>
</body>
</html>
```